Design the Mobile Version of Existing Web Based Health Platform

Loomcrest is a social business enterprise that focus on public health by applying innovative healthcare services and consumer internet technology. Loomcrest offers a personalized platform of health promotion and disease prevention that puts the individual back in control of his life.

Loomcrest is looking for a Mobile Web UX/Visual Design professional to create a mobile version of Loomcrest website platform for iPhone, iPad/tablet and Android.

Contestants must to check www.loomcrest-demo.com.br to have a better understanding of Loomcrest Platform by creating an account (it's in portuguese, but anyone can get the general idea).

The mobile version of Loomcrest should have very similar functionality and user flows. This job is not to reengineer or re-imagine Loomcrest. It is just to reformat the existing functionality so it works well on mobile devices.

This description below is to help you to understand the core features of the platform (check the attachments to see the new web design of each one):

- Personally Controlled Health Record - PCHR enables an individual to own and manage a complete, secure, digital copy of her health and wellness information.
- Health Risk Assessments - is a process to estimate the nature and probability of adverse health effects, based on personal and family historical data, behavior and environment.
- Simulation of future health - "what if analysis" that emphasizes health education and behavior change.
- Step Quests - a program that gives you the opportunity to the participant to advance his personal well-being by doing simple Step Quests
- Health Alerts and Recommendations and Missing Data - Recommendations based on Wellbeing Bureau Guidelines and Federal Wellness Review Panel (FWRP), plus notifications to update outdated information.

The deliverable for this project is a psd file with a designed mobile version of Loomcrest.

A new design of the web platform is under construction. You can also check it looking at the files attached.

Target Market(s)

people 25-40 years old, 60% female, socially engaged

Industry/Entity Type

Healthcare

Requirements
Must have
• iPhone, iPad and Android version

Design must cover all current functionalities available on the web version (please, ensure you understand all features by creating an account at www.loomcrest-demo.com.br)

- Login/Sign up
- Welcome (first assessment)
- Add to Personal Controlled Health Record (PCHR)
- Update/Remove PCHR
- List PCHR
- Riskgrid (risk assessmen results)
- Simulation
- Alerts
- Missing data
- Recommendations
- StepQuest
- Badges
- Configurations

It's important to check the attachments to see how the web platform design is evolving.

```html
<!DOCTYPE html>
<html lang="pt">
<head>
<meta charset="utf-8">
<title>Loomcrest Mobile</title>
<link rel="stylesheet" href="https://fonts.googleapis.com/css2?family=Roboto:wght@300;400;700&display=swap">
<style>
:root{
  --stage:#2e2e2e;
  --bar:#3a3a3a;
  --bar-dark:#262626;
  --green:#8cc63f;
  --green-dark:#6a9e1f;
  --orange:#f7941d;
  --orange-soft:#fbb040;
  --red:#e8292b;
  --grey-band:#4a4a4a;
  --text:#555;
  --white:#fff;
}
*{box-sizing:border-box;margin:0;padding:0}
html,body{width:1200px;height:590px;overflow:hidden}
body{background:var(--stage);font-family:"Roboto",Helvetica,Arial,sans-serif;position:relative}
.screen{position:absolute;top:140px;width:180px;height:268px;overflow:hidden;background:var(--white)}
.screen--home{left:66px}
.screen--menu{left:291px}
.screen--risk{left:515px}
.screen--bodymap{left:742px}
.screen--reduce{left:968px}
.abs{position:absolute}
.backdrop{position:absolute;inset:0;background:linear-gradient(160deg,#f4ecd8 0%,#e9d7c9 30%,#b98fb4 58%,#5d6fb0 80%,#3e5a9a 100%)}
.topbar{position:absolute;left:0;top:0;width:180px;height:24px;background:linear-gradient(#4a4a4a,#2a2a2a);display:flex;align-items:center}
.back-btn{position:absolute;left:6px;top:5px;width:20px;height:14px;background:#111;border-radius:3px;box-shadow:0 0 0 1px #555}
.back-btn svg{display:block;margin:2px auto}
.user-name{position:absolute;right:52px;top:8px;font-size:6.5px;color:#bbb;letter-spacing:.2px}
.user-name b{color:var(--green);font-weight:700}
.user-photo{position:absolute;right:22px;top:0;width:28px;height:24px;background:linear-gradient(#9a9a9a,#5e5e5e)}
.badge{position:absolute;right:6px;top:6px;width:11px;height:12px;background:var(--red);color:#fff;font-size:8px;text-align:center;line-height:12px;border-radius:2px}
.tile{position:absolute;width:56px;height:56px;background:linear-gradient(#fff,#e4e4e4);border-radius:7px;box-shadow:0 1px 3px rgba(0,0,0,.4);text-align:center}
.tile svg{margin-top:8px}
.tile-label{position:absolute;bottom:4px;left:0;width:100%;font-size:6.5px;font-weight:700;color:#333}
.settings-link{position:absolute;right:20px;bottom:5px;font-size:6px;color:#fff;display:flex;align-items:center;gap:3px}
.menu-item{position:absolute;left:0;width:180px;display:flex;align-items:center;color:#fff}
.menu-item .chev{position:absolute;left:6px}
.menu-item--risk{top:55px;height:48px;background:linear-gradient(var(--green),#79b22d)}
.menu-item--body{top:103px;height:32px;background:var(--orange)}
.menu-item--reduce{top:135px;height:25px;background:var(--grey-band)}
.menu-title-big{font-size:26px;font-weight:300;position:absolute;left:72px;top:9px}
.menu-title{font-size:11.5px;font-weight:300;position:absolute;left:70px}
.header{position:absolute;left:0;top:0;width:180px;height:40px;color:#fff}
.header--green{background:linear-gradient(var(--green),#7fb834)}
.header--orange{background:var(--orange)}
.header--grey{height:50px;background:linear-gradient(#4d4d4d,#333)}
.header .back-btn{top:12px;left:6px}
.header-title{position:absolute;font-weight:300}
.strip{position:absolute;left:0;width:180px;font-size:6.5px;font-weight:700;text-align:center;color:#fff}
.strip--orange{top:40px;height:12px;line-height:12px;background:var(--orange-soft);color:#fff5e0}
.strip--green{top:50px;height:12px;line-height:12px;background:var(--green)}
.risk-value{position:absolute;left:10px;top:62px;color:var(--red);font-size:26px;font-weight:300}
.risk-value sup{font-size:12px}
.scale-label{position:absolute;font-size:9px;color:#666}
.risk-summary{position:absolute;left:6px;top:218px;width:170px;font-size:7px;font-weight:700;color:var(--green);line-height:1.2}
.risk-summary .hi{font-size:9px}
.risk-summary .muted{color:#777;font-weight:400;font-size:6px}
.risk-note{position:absolute;left:6px;top:238px;width:170px;font-size:4.6px;color:#777;line-height:1.35}
.risk-note a{color:var(--orange);font-weight:700;text-decoration:none}
.risk-list{position:absolute;left:10px;top:56px;list-style:none}
.risk-list li{display:flex;align-items:center;gap:6px;height:20px;font-size:4.8px;color:#777}
.risk-list .mark{width:8px;height:14px;background:#e4e6ea}
.risk-list .mark--active{background:var(--orange)}
.body-figure{position:absolute;left:104px;top:48px;width:66px;height:210px;border-radius:30px 30px 8px 8px;background:radial-gradient(circle at 52% 30%,rgba(247,148,29,.55) 0 6px,transparent 9px),radial-gradient(circle at 28% 60%,rgba(247,148,29,.5) 0 4px,transparent 7px),linear-gradient(#fff4e6,#fde3c3)}
.legend{position:absolute;left:10px;top:196px;list-style:none}
.legend li{display:flex;align-items:center;gap:4px;height:11px;font-size:4.8px;color:#777}
.legend .dot{width:5px;height:5px;border-radius:50%}
.tips{position:absolute;left:12px;top:108px;list-style:none}
.tips li{display:flex;align-items:center;gap:8px;height:38px;font-size:7px;font-weight:700;line-height:1.25}
.tips .check{width:28px;height:28px;border:2.5px solid var(--green-dark);background:#fff;display:flex;align-items:center;justify-content:center}
.tips .t1{color:var(--orange)}
.tips .t2{color:var(--green-dark)}
.fade-bottom{position:absolute;left:0;bottom:0;width:180px;height:30px;background:linear-gradient(rgba(255,255,255,0),#e6e6e6)}
</style>
</head>
<body>

<!-- Home -->
<section class="screen screen--home">
  <div class="backdrop" role="img" aria-label="Soft blurred flower field in cream, pink and blue tones"></div>
  <div class="topbar">
    <span class="back-btn"><svg width="10" height="9" viewBox="0 0 10 9"><path d="M1 1h5M1 1v5M1 1l7 7" stroke="#fff" stroke-width="1.6" fill="none"/></svg></span>
    <span class="user-name">RAFAEL <b>MONTEIRO</b></span>
    <span class="user-photo" role="img" aria-label="User profile photo"></span>
    <span class="badge">2</span>
  </div>
  <div class="tile" style="left:24px;top:52px">
    <svg width="34" height="26" viewBox="0 0 34 26"><path d="M3 24 A16 16 0 0 1 31 10" stroke="#555" stroke-width="5" fill="none"/><path d="M5 24 L24 6" stroke="#333" stroke-width="2"/></svg>
    <span class="tile-label">Health Map</span>
  </div>
  <div class="tile" style="left:104px;top:52px">
    <svg width="28" height="28" viewBox="0 0 28 28"><circle cx="14" cy="14" r="12" fill="#666"/><path d="M7 12a7 7 0 0 1 13-2M21 16a7 7 0 0 1-13 2" stroke="#fff" stroke-width="2.2" fill="none"/><path d="M20 6v5h-5M8 22v-5h5" stroke="#fff" stroke-width="2" fill="none"/></svg>
    <span class="tile-label">Simulation</span>
  </div>
  <div class="tile" style="left:24px;top:120px">
    <svg width="26" height="30" viewBox="0 0 26 30"><circle cx="13" cy="11" r="9" fill="#666"/><circle cx="13" cy="11" r="5" fill="#ddd"/><path d="M8 18l-3 10 5-3 3 4M18 18l3 10-5-3-3 4" fill="#555"/></svg>
    <span class="tile-label">Challenges</span>
  </div>
  <div class="tile" style="left:104px;top:120px">
    <svg width="24" height="30" viewBox="0 0 24 30"><rect x="2" y="3" width="20" height="26" rx="2" fill="#555"/><rect x="5" y="7" width="14" height="19" fill="#fff"/><rect x="8" y="1" width="8" height="5" rx="1" fill="#333"/><path d="M7 12h10M7 16h10M7 20h7" stroke="#666"/></svg>
    <span class="tile-label">Booklet</span>
  </div>
  <div class="tile" style="left:24px;top:188px">
    <svg width="28" height="28" viewBox="0 0 28 28"><path d="M7 3h14v8a7 7 0 0 1-14 0z" fill="#666"/><path d="M7 6H3a4 4 0 0 0 5 6M21 6h4a4 4 0 0 1-5 6" stroke="#666" stroke-width="2" fill="none"/><path d="M12 17h4v5h-4z" fill="#555"/><rect x="8" y="22" width="12" height="4" fill="#444"/><path d="M14 5l1.2 2.5 2.7.3-2 1.8.6 2.6-2.5-1.4-2.5 1.4.6-2.6-2-1.8 2.7-.3z" fill="#ddd"/></svg>
    <span class="tile-label">Trophies</span>
  </div>
  <div class="tile" style="left:104px;top:188px">
    <svg width="30" height="24" viewBox="0 0 30 24"><rect x="1" y="8" width="8" height="8" fill="#555"/><rect x="11" y="8" width="8" height="8" fill="#555"/><rect x="21" y="8" width="8" height="8" fill="#555"/></svg>
    <span class="tile-label">More</span>
  </div>
  <span class="settings-link"><svg width="8" height="8" viewBox="0 0 8 8"><circle cx="4" cy="4" r="3" stroke="var(--green)" stroke-width="1.6" fill="none" stroke-dasharray="1.2 .6"/><circle cx="4" cy="4" r="1" fill="var(--green)"/></svg>CONFIGURAÇÕE</span>
</section>

<!-- Menu -->
<section class="screen screen--menu">
  <div class="backdrop" role="img" aria-label="Soft blurred flower field in pink, lilac and blue tones"></div>
  <div class="topbar">
    <span class="back-btn"><svg width="10" height="9" viewBox="0 0 10 9"><path d="M1 1h5M1 1v5M1 1l7 7" stroke="#fff" stroke-width="1.6" fill="none"/></svg></span>
    <span class="user-name">RAFAEL <b>MONTEIRO</b></span>
    <span class="user-photo" role="img" aria-label="User profile photo"></span>
    <span class="badge">2</span>
  </div>
  <div class="menu-item menu-item--risk">
    <svg class="chev" width="6" height="8" viewBox="0 0 6 8"><path d="M1 1l3 3-3 3" stroke="#333" stroke-width="1.6" fill="none"/></svg>
    <svg class="abs" style="left:18px;top:8px" width="48" height="32" viewBox="0 0 48 32"><path d="M4 28 A20 20 0 0 1 36 10" stroke="rgba(255,255,255,.55)" stroke-width="6" fill="none"/><path d="M6 28 L26 10" stroke="#fff" stroke-width="2"/><text x="30" y="30" font-size="11" fill="#fff" font-family="Roboto,sans-serif">%</text></svg>
    <span class="menu-title-big">RISCO</span>
  </div>
  <div class="menu-item menu-item--body">
    <svg class="chev" width="6" height="8" viewBox="0 0 6 8"><path d="M1 1l3 3-3 3" stroke="#333" stroke-width="1.6" fill="none"/></svg>
    <svg class="abs" style="left:26px;top:3px" width="26" height="26" viewBox="0 0 26 26"><circle cx="13" cy="13" r="11.5" fill="none" stroke="#fff" stroke-width="2"/><circle cx="13" cy="7" r="2.5" fill="#fff"/><path d="M9 11h8v6h-2v6h-4v-6H9z" fill="#fff"/></svg>
    <span class="menu-title">Mapa do corpo</span>
  </div>
  <div class="menu-item menu-item--reduce">
    <svg class="chev" width="6" height="8" viewBox="0 0 6 8"><path d="M1 1l3 3-3 3" stroke="#ccc" stroke-width="1.6" fill="none"/></svg>
    <svg class="abs" style="left:24px;top:3px" width="28" height="20" viewBox="0 0 28 20"><rect x="2" y="8" width="12" height="9" fill="#bbb"/><path d="M5 10l6 5M11 10l-6 5" stroke="#666" stroke-width="1.2"/><rect x="12" y="1" width="13" height="11" fill="var(--orange)"/><path d="M15 6l3 3 5-6" stroke="#fff" stroke-width="1.8" fill="none"/></svg>
    <span class="menu-title">Reduzir o seu risco</span>
  </div>
</section>

<!-- Risk -->
<section class="screen screen--risk">
  <div class="header header--green">
    <span class="back-btn"><svg width="10" height="9" viewBox="0 0 10 9"><path d="M1 1h5M1 1v5M1 1l7 7" stroke="#fff" stroke-width="1.6" fill="none"/></svg></span>
    <svg class="abs" style="left:34px;top:4px" width="46" height="32" viewBox="0 0 46 32"><path d="M4 28 A20 20 0 0 1 36 10" stroke="rgba(255,255,255,.55)" stroke-width="6" fill="none"/><path d="M6 28 L26 10" stroke="#fff" stroke-width="2"/><text x="28" y="30" font-size="11" fill="#fff" font-family="Roboto,sans-serif">%</text></svg>
    <span class="header-title" style="left:88px;top:5px;font-size:25px">RISCO</span>
  </div>
  <div class="strip strip--orange">Risco de cancer colorretal : 0.28%</div>
  <div class="risk-value">28<sup>%</sup></div>
  <svg class="abs" style="left:0;top:0" width="180" height="268" viewBox="0 0 180 268">
    <defs>
      <linearGradient id="gaugeFill" x1="0" x2="1" y1="0" y2="0">
        <stop offset="0" stop-color="#3c9a2a"/>
        <stop offset=".35" stop-color="#d6e03a"/>
        <stop offset=".65" stop-color="#f7941d"/>
        <stop offset="1" stop-color="#e8292b"/>
      </linearGradient>
    </defs>
    <path d="M11 190 A160 98 0 0 1 171 92 L171 120 A145 70 0 0 0 26 190 Z" fill="url(#gaugeFill)"/>
    <path d="M80 194 L14 104 L87 187 Z" fill="#333"/>
    <circle cx="83" cy="190" r="8" fill="#444"/>
    <circle cx="83" cy="190" r="3.5" fill="#999"/>
  </svg>
  <span class="scale-label" style="left:23px;top:182px">0</span>
  <span class="scale-label" style="left:145px;top:163px">100</span>
  <p class="risk-summary">Risco abaixo da média <span class="hi" style="color:var(--orange)">28%</span> <span class="muted">das mulheres de sua idade têm um risco menor.</span></p>
  <p class="risk-note">É importante conhecer, com maior precisão, o risco de você ser diagnosticado com derrame cerebral nos próximos 5 anos. Para isso, elimine os dados pendentes de sua caderneta.... <a href="#">More</a></p>
</section>

<!-- Body map -->
<section class="screen screen--bodymap">
  <div class="header header--orange">
    <span class="back-btn"><svg width="10" height="9" viewBox="0 0 10 9"><path d="M1 1h5M1 1v5M1 1l7 7" stroke="#fff" stroke-width="1.6" fill="none"/></svg></span>
    <svg class="abs" style="left:38px;top:5px" width="30" height="30" viewBox="0 0 26 26"><circle cx="13" cy="13" r="11.5" fill="none" stroke="#fff" stroke-width="2"/><circle cx="13" cy="7" r="2.5" fill="#fff"/><path d="M9 11h8v6h-2v6h-4v-6H9z" fill="#fff"/></svg>
    <span class="header-title" style="left:80px;top:13px;font-size:12px">Mapa do corpo</span>
  </div>
  <ul class="risk-list">
    <li><span class="mark mark--active"></span>Risco de arterial coronariana : 0,15%</li>
    <li><span class="mark"></span>Risco de derrame cerebral : 0,25%</li>
    <li><span class="mark"></span>Risco de cancer : 0,13%</li>
    <li><span class="mark"></span>Risco de diabetes : 0,26%</li>
  </ul>
  <div class="body-figure" role="img" aria-label="Orange outline of a human body with highlighted risk areas at chest, abdomen and leg"></div>
  <ul class="legend">
    <li><span class="dot" style="background:#f26522"></span>Condição pré-existente</li>
    <li><span class="dot" style="background:#e8292b"></span>Alto</li>
    <li><span class="dot" style="background:#f7941d"></span>Acima da Média</li>
    <li><span class="dot" style="background:#f9d423"></span>Na Média</li>
    <li><span class="dot" style="background:#8cc63f"></span>Abaixo da Média</li>
    <li><span class="dot" style="background:#3c7a1e"></span>Baixo</li>
  </ul>
</section>

<!-- Reduce risk -->
<section class="screen screen--reduce">
  <div class="header header--grey">
    <span class="back-btn" style="top:16px"><svg width="10" height="9" viewBox="0 0 10 9"><path d="M1 1h5M1 1v5M1 1l7 7" stroke="#fff" stroke-width="1.6" fill="none"/></svg></span>
    <svg class="abs" style="left:38px;top:10px" width="38" height="30" viewBox="0 0 38 30"><rect x="2" y="12" width="18" height="13" fill="#bbb"/><path d="M6 15l9 7M15 15l-9 7" stroke="#666" stroke-width="1.5"/><rect x="16" y="2" width="18" height="15" fill="var(--orange)"/><path d="M20 9l4 4 7-8" stroke="#fff" stroke-width="2.2" fill="none"/></svg>
    <span class="header-title" style="left:82px;top:12px;font-size:11.5px;line-height:1.15">Reduzir o seu<br>risco</span>
  </div>
  <div class="strip strip--green">Você pode reduzir o seu risco em 0.30%</div>
  <ul class="tips">
    <li><span class="check"><svg width="18" height="14" viewBox="0 0 18 14"><path d="M2 7l5 5 9-10" stroke="var(--green-dark)" stroke-width="3" fill="none"/></svg></span><span><span class="t1">Reduza seu risco</span><br><span class="t2">Praticando atividades físicas</span></span></li>
    <li><span class="check"><svg width="18" height="14" viewBox="0 0 18 14"><path d="M2 7l5 5 9-10" stroke="var(--green-dark)" stroke-width="3" fill="none"/></svg></span><span><span class="t1">Reduza seu risco</span><br><span class="t2">Praticando atividades físicas</span></span></li>
    <li><span class="check"><svg width="18" height="14" viewBox="0 0 18 14"><path d="M2 7l5 5 9-10" stroke="var(--green-dark)" stroke-width="3" fill="none"/></svg></span><span><span class="t1">Reduza seu risco</span><br><span class="t2">Praticando atividades físicas</span></span></li>
  </ul>
  <div class="fade-bottom"></div>
</section>

</body>
</html>
```